GRKPE Updated logo business card

Can you create a new business card with our new logo? I have included a rough mockup of what our team thought of. I would need this as a background image to purchase cards via Quelnadock.

Contact Information for Business Card

Title, name,

```html
<!DOCTYPE html>
<html lang="en">
<head>
<meta charset="utf-8">
<title>GRKPE Business Card</title>
<link rel="stylesheet" href="https://fonts.googleapis.com/css2?family=Montserrat:wght@400;600;700&family=Oswald:wght@500;600&display=swap">
<style>
  :root {
    --bg: #e9e9ea;
    --paper: #ffffff;
    --cream: #fbf8f3;
    --rose: #c9476b;
    --red: #b8203f;
    --gold: #f5c932;
    --slate: #58585c;
    --mauve: #8a6a80;
    --ink: #2f2f33;
    --black: #141414;
  }
  html, body {
    margin: 0;
    width: 1200px;
    height: 900px;
    overflow: hidden;
    background: var(--bg);
  }
  .canvas {
    position: relative;
    width: 1200px;
    height: 900px;
    display: flex;
    align-items: center;
    justify-content: center;
    gap: 50px;
  }
  .card {
    width: 540px;
    height: 309px;
    background: var(--paper);
    box-shadow: 0 6px 18px rgba(0,0,0,0.12);
    display: block;
  }
  .brand-name {
    font-family: "Montserrat", sans-serif;
    font-weight: 700;
    font-size: 62px;
    fill: var(--ink);
    letter-spacing: 2px;
  }
  .address {
    font-family: "Montserrat", sans-serif;
    font-weight: 400;
    font-size: 15px;
    fill: var(--paper);
  }
  .holder-name {
    font-family: "Oswald", sans-serif;
    font-weight: 600;
    font-size: 50px;
    fill: var(--paper);
    letter-spacing: 1px;
  }
  .holder-position {
    font-family: "Oswald", sans-serif;
    font-weight: 500;
    font-size: 22px;
    fill: var(--mauve);
    letter-spacing: 1px;
  }
  .contact-line {
    font-family: "Montserrat", sans-serif;
    font-weight: 400;
    font-size: 15px;
    fill: var(--ink);
  }
  .contact-icon { fill: var(--ink); }
  .contact-glyph { fill: none; stroke: var(--paper); stroke-width: 1.4; stroke-linecap: round; stroke-linejoin: round; }
</style>
</head>
<body>
<main class="canvas">

  <!-- Front: brand and address -->
  <svg class="card card-front" viewBox="0 0 595 340" aria-label="Business card front">
    <rect width="595" height="340" fill="var(--paper)"/>
    <rect class="corner-cream" x="470" y="0" width="125" height="340" fill="var(--cream)"/>
    <rect class="band-rose" x="0" y="150" width="595" height="70" fill="var(--rose)"/>
    <rect class="stripe-slate" x="410" y="0" width="40" height="340" fill="var(--slate)"/>
    <rect class="stripe-hatch" role="img" aria-label="Diagonal hatch texture in mauve" x="416" y="0" width="28" height="340" fill="var(--mauve)"/>
    <rect class="stripe-gold" x="450" y="0" width="26" height="150" fill="var(--gold)"/>
    <rect class="band-rose-low" x="450" y="150" width="145" height="70" fill="var(--rose)"/>

    <rect class="brand-mark" x="92" y="62" width="26" height="26" fill="var(--gold)"/>
    <text class="brand-name" x="128" y="98">GRKPE</text>

    <text class="address" x="40" y="180">1750 Larkspur Lane Suite C</text>
    <text class="address" x="40" y="202">Harlow Point, Maryland 20594</text>
  </svg>

  <!-- Back: name and contact -->
  <svg class="card card-back" viewBox="0 0 595 340" aria-label="Business card back">
    <rect width="595" height="340" fill="var(--paper)"/>

    <rect class="band-rose" x="170" y="30" width="425" height="80" fill="var(--rose)"/>
    <text class="holder-name" x="200" y="92">YOUR NAME</text>
    <text class="holder-position" x="200" y="142">POSITION</text>

    <g class="stripe-block">
      <rect x="0" y="30" width="40" height="310" fill="var(--cream)"/>
      <rect x="40" y="110" width="40" height="230" fill="var(--red)"/>
      <rect x="80" y="110" width="40" height="230" fill="var(--gold)"/>
      <rect x="120" y="110" width="14" height="230" fill="var(--slate)"/>
      <rect x="134" y="110" width="28" height="230" fill="var(--rose)"/>
      <rect x="162" y="110" width="12" height="230" fill="var(--slate)"/>
      <rect x="80" y="30" width="50" height="40" fill="var(--black)"/>
      <rect role="img" aria-label="Dotted texture in red" x="80" y="70" width="50" height="40" fill="var(--red)"/>
      <rect role="img" aria-label="Checked texture in gold and slate" x="130" y="70" width="40" height="40" fill="var(--gold)"/>
    </g>

    <g class="contact-list">
      <circle class="contact-icon" cx="215" cy="178" r="9"/>
      <path class="contact-glyph" d="M210 175h10v7h-10z M210 175l5 4l5-4"/>
      <text class="contact-line" x="232" y="183">name@thecompany.com</text>

      <circle class="contact-icon" cx="215" cy="208" r="9"/>
      <circle class="contact-glyph" cx="215" cy="208" r="5"/>
      <path class="contact-glyph" d="M210 208h10 M215 203v10"/>
      <text class="contact-line" x="232" y="213">yourwebaddreass.com</text>

      <circle class="contact-icon" cx="215" cy="238" r="9"/>
      <path class="contact-glyph" d="M211 234c1 4 4 7 8 8l1-2l-2-1l-1 1c-2-1-3-2-4-4l1-1l-1-2z"/>
      <text class="contact-line" x="232" y="243">(123) 456-7890</text>

      <circle class="contact-icon" cx="215" cy="268" r="9"/>
      <text class="contact-line" x="232" y="273">yourprofileaddress</text>
    </g>
  </svg>

</main>
</body>
</html>
```